Veltarum

Standard Business Card design.
Sample two-sided design uploaded. White front, Black back.
Would like white shield to be on all black background side.
Willing to look at a couple creative designs, but nothing crazy.
Preference for a classic, confident, strong design.

```html
<!DOCTYPE html>
<html lang="en">
<head>
<meta charset="utf-8">
<title>Veltarum Business Card</title>
<link rel="stylesheet" href="https://fonts.googleapis.com/css2?family=Arimo:wght@400;700&display=swap">
<style>
  :root {
    --backdrop: #e8e8e6;
    --card-white: #ffffff;
    --card-black: #1d1d1d;
    --ink: #1a1a1a;
    --ink-soft: #2a2a2a;
    --faint: #ececec;
    --paper-light: #ffffff;
  }
  * { margin: 0; padding: 0; box-sizing: border-box; }
  html, body {
    width: 1200px;
    height: 1000px;
    overflow: hidden;
    background: var(--backdrop);
    font-family: "Arimo", Arial, sans-serif;
  }
  .canvas {
    position: relative;
    width: 1200px;
    height: 1000px;
  }
  .card {
    position: absolute;
    width: 524px;
    height: 300px;
    overflow: hidden;
  }
  .card-front {
    left: 600px;
    top: 120px;
    background: var(--card-white);
    color: var(--ink);
  }
  .card-back {
    left: 157px;
    top: 515px;
    background: var(--card-black);
    display: flex;
    align-items: center;
    justify-content: center;
  }
  .brand {
    position: absolute;
    left: 34px;
    top: 32px;
    display: flex;
    align-items: center;
    gap: 10px;
  }
  .brand-square {
    width: 22px;
    height: 22px;
    background: var(--ink);
  }
  .brand-name {
    font-size: 22px;
    font-weight: 700;
    letter-spacing: 2px;
    text-transform: uppercase;
    color: var(--ink);
  }
  .person {
    position: absolute;
    left: 34px;
    top: 108px;
    line-height: 1.15;
  }
  .person-name {
    font-size: 17px;
    font-weight: 700;
  }
  .person-role {
    font-size: 17px;
    font-weight: 400;
    color: var(--ink-soft);
  }
  .contact {
    position: absolute;
    left: 34px;
    top: 180px;
    list-style: none;
    font-size: 17px;
    line-height: 1.15;
    color: var(--ink-soft);
  }
  .watermark-name {
    position: absolute;
    right: 28px;
    bottom: 28px;
    font-size: 46px;
    font-weight: 700;
    letter-spacing: 2px;
    line-height: 1;
    text-transform: uppercase;
    color: var(--faint);
    white-space: nowrap;
  }
  .back-name {
    font-size: 34px;
    font-weight: 700;
    letter-spacing: 4px;
    text-transform: uppercase;
    color: var(--paper-light);
  }
</style>
</head>
<body>
  <main class="canvas">
    <section class="card card-front" aria-label="Business card front">
      <span class="watermark-name" aria-hidden="true">Veltarum</span>
      <div class="brand">
        <span class="brand-square"></span>
        <span class="brand-name">Veltarum</span>
      </div>
      <div class="person">
        <p class="person-name">Name Surname</p>
        <p class="person-role">Position</p>
      </div>
      <ul class="contact">
        <li>name@website.com</li>
        <li>website.com</li>
        <li>123-456-7890</li>
      </ul>
    </section>

    <section class="card card-back" aria-label="Business card back">
      <span class="back-name">Veltarum</span>
    </section>
  </main>
</body>
</html>
```